Redesign of iOS App Lumo Tutor

Redesign of existing App Lumo Tutor, an app that helps learning Japanese Kanjis, Hiragana, Katakana.

The functionallity should remain the same as today: the app is free, you may download it at the app store. But: I like the design of my other apps better ;)

Target Market(s)

Students learning Japanese

Industry/Entity Type

Teacher

Font styles to use
Sans Serif

Requirements
Must have
• Lumo Tutor has 7 main screens, all screens has to be designed for iPhone and iPad: Main, Settings, Reading Tests, Writing Tests, Game, Paper Mode, Search
Nice to have
• I like the logo as it is today

```html
<!DOCTYPE html>
<html lang="en">
<head>
<meta charset="utf-8">
<title>Lumo Tutor – Settings</title>
<link href="https://fonts.googleapis.com/css2?family=Nunito:wght@400;600;700&display=swap" rel="stylesheet">
<style>
  :root {
    --bg: #ffffff;
    --ink: #3a3a3a;
    --ink-soft: #444444;
    --rule: #9a9a9a;
    --option-fill: #f2f2f4;
    --option-border: #cfcfcf;
    --selected-fill: #9b9b9b;
    --selected-border: #8e8e8e;
    --credit: #a9a9a9;
  }
  * { box-sizing: border-box; margin: 0; padding: 0; }
  html, body { width: 675px; height: 1200px; overflow: hidden; background: var(--bg); }
  body { font-family: "Nunito", sans-serif; color: var(--ink); position: relative; }

  .status-bar { position: absolute; top: 0; left: 0; width: 675px; height: 36px;
    display: flex; align-items: center; justify-content: space-between;
    padding: 0 10px; font-size: 18px; font-family: "Nunito", sans-serif; color: #111; }
  .status-left, .status-right { display: flex; align-items: center; gap: 6px; width: 140px; }
  .status-right { justify-content: flex-end; }
  .status-time { font-weight: 600; }

  .setting-group { position: absolute; left: 35px; width: 604px; }
  .group-title { display: flex; align-items: center; gap: 22px; height: 28px;
    font-size: 23.5px; font-weight: 400; letter-spacing: 0.4px; white-space: nowrap; }
  .group-title::before, .group-title::after { content: ""; flex: 1; height: 1.5px; background: var(--rule); }

  .options { display: flex; gap: 35px; margin-top: 13px; }
  .options.three { gap: 31px; }
  .option { flex: 1; height: 54px; border-radius: 15px; border: 1.5px solid var(--option-border);
    background: var(--option-fill); display: flex; align-items: center; justify-content: center;
    font-size: 20px; font-weight: 700; letter-spacing: 0.5px; color: var(--ink); }
  .option.is-selected { background: var(--selected-fill); border-color: var(--selected-border);
    color: var(--ink-soft); font-weight: 600; }

  .credits { position: absolute; top: 1001px; left: 0; width: 675px; text-align: center;
    font-size: 23px; color: var(--credit); letter-spacing: 0.5px; }

  .home-button { position: absolute; left: 35px; top: 1094px; width: 137px; height: 54px;
    border: 1.5px solid var(--option-border); border-radius: 3px; background: var(--option-fill);
    display: flex; align-items: center; justify-content: center; font-size: 20px; font-weight: 700; }
</style>
</head>
<body>
  <header class="status-bar">
    <div class="status-left">
      <svg width="68" height="12" viewBox="0 0 68 12" aria-hidden="true">
        <g fill="#111"><circle cx="5" cy="6" r="5"/><circle cx="17" cy="6" r="5"/><circle cx="29" cy="6" r="5"/><circle cx="41" cy="6" r="5"/><circle cx="53" cy="6" r="5"/></g>
      </svg>
      <svg width="20" height="15" viewBox="0 0 20 15" aria-hidden="true">
        <path d="M10 14 L6.5 10.2 A5 5 0 0 1 13.5 10.2 Z" fill="#111"/>
        <path d="M3.5 7.2 A9.5 9.5 0 0 1 16.5 7.2" stroke="#111" stroke-width="2.2" fill="none"/>
        <path d="M0.8 4.2 A13.5 13.5 0 0 1 19.2 4.2" stroke="#111" stroke-width="2.2" fill="none"/>
      </svg>
    </div>
    <span class="status-time">9:41 AM</span>
    <div class="status-right">
      <span>100%</span>
      <svg width="42" height="18" viewBox="0 0 42 18" aria-hidden="true">
        <rect x="0.75" y="0.75" width="37" height="16.5" rx="3" fill="none" stroke="#111" stroke-width="1.5"/>
        <rect x="3" y="3" width="32.5" height="12" rx="1.5" fill="#111"/>
        <rect x="39" y="6" width="2.5" height="6" rx="1" fill="#111"/>
      </svg>
    </div>
  </header>

  <section class="setting-group" style="top:85px">
    <h2 class="group-title">Group Tests by</h2>
    <div class="options">
      <div class="option is-selected">JLPT Level</div>
      <div class="option">School Year</div>
    </div>
  </section>

  <section class="setting-group" style="top:234px">
    <h2 class="group-title">Size of Answer Grid</h2>
    <div class="options">
      <div class="option is-selected">3 x 3</div>
      <div class="option">4 x 4</div>
    </div>
  </section>

  <section class="setting-group" style="top:385px">
    <h2 class="group-title">Show Meaning in Test</h2>
    <div class="options three">
      <div class="option">Never</div>
      <div class="option is-selected">Classic</div>
      <div class="option">Always</div>
    </div>
  </section>

  <section class="setting-group" style="top:536px">
    <h2 class="group-title">Show Pattern in Writing Tests</h2>
    <div class="options three">
      <div class="option">Never</div>
      <div class="option is-selected">Classic</div>
      <div class="option">Always</div>
    </div>
  </section>

  <section class="setting-group" style="top:688px">
    <h2 class="group-title">Tests used in Game</h2>
    <div class="options three">
      <div class="option">Meaning</div>
      <div class="option">Reading</div>
      <div class="option is-selected">Both</div>
    </div>
  </section>

  <section class="setting-group" style="top:838px">
    <h2 class="group-title">Feedback</h2>
    <div class="options">
      <div class="option">Rate</div>
      <div class="option">E-Mail</div>
    </div>
  </section>

  <p class="credits">many thanks to lexiconhub.net and strokeset.info</p>

  <div class="home-button">Home</div>
</body>
</html>
```